Web design for Money Service Business (uncoded)

We need a very basic website with 5-6 pages. Home page, Services, Transfer(How to use our service), About us, Contact us, FAQ
Our company name is Meridale Exchange. We are a company that deals with currency exchange and international money transfer. We do cash exchange and international money transfers to bank accounts all over the world. We offer highly competitive exchange rates so usually attract customers who transfer money over $10,000. Our niche is with larger sums of money, the design needs to be professional and communicate trust, security and stability.

```html
<!DOCTYPE html>
<html lang="en">
<head>
<meta charset="utf-8">
<title>Meridale Exchange — International Money Transfer</title>
<link rel="stylesheet" href="https://fonts.googleapis.com/css2?family=Montserrat:wght@400;500;600;700&family=Arimo:wght@400&display=swap">
<style>
:root{
  --blue-dark:#1b578a;
  --blue:#1f6aa5;
  --link:#1a8fd6;
  --orange:#f29a1f;
  --orange-light:#ffc43a;
  --text:#3a3a3a;
  --muted:#666;
  --rule:#d9d9d9;
  --hero-a:#2f86c2;
  --hero-b:#8fd0ef;
}
*{box-sizing:border-box;margin:0;padding:0}
html,body{width:1060px;height:1200px;overflow:hidden;background:#fff}
body{position:relative;font-family:"Montserrat",sans-serif;color:var(--text)}
.page{position:relative;width:1060px;height:1200px}
.abs{position:absolute}

/* header */
.header-band{left:0;top:0;width:1060px;height:126px;background:linear-gradient(#ffffff,#ececec);border-bottom:1px solid #dcdcdc}
.brand{left:124px;top:24px;display:flex;flex-direction:column}
.brand-name{font-size:30px;font-weight:600;color:var(--blue-dark);letter-spacing:.5px;line-height:40px;display:flex;align-items:center;gap:10px}
.brand-dot{width:20px;height:20px;border-radius:50%;background:var(--orange)}
.brand-tag{font-size:14px;letter-spacing:3.2px;color:#8a9aa8;margin-top:4px;white-space:nowrap}
.help-top{right:126px;top:46px;text-align:right;font-family:"Arimo",sans-serif;font-size:12px;line-height:20px;color:#222}
.help-top a{color:var(--link);text-decoration:none}
.help-top .tel{color:var(--orange)}

/* nav */
.nav{left:124px;top:104px;width:810px;height:43px;border-radius:3px;background:linear-gradient(#22659c,#174e7c);display:flex}
.nav a{display:flex;align-items:center;padding:0 15px;height:43px;color:#fff;text-decoration:none;font-size:15.5px;font-weight:500;border-right:1px solid #2f6f9f}
.nav a.active{background:linear-gradient(#f6a93a,#e38a14);padding:0 20px;border-radius:3px 0 0 3px}
.login{left:843px;top:109px;width:84px;height:32px;border-radius:4px;background:linear-gradient(#2ea6ee,#1377c6);border:1px solid #0e5d9c;color:#fff;font-weight:700;font-size:15px;display:flex;align-items:center;justify-content:center;letter-spacing:.5px}

/* hero */
.hero{left:124px;top:164px;width:810px;height:319px;border-radius:3px;overflow:hidden;background:linear-gradient(100deg,var(--hero-a) 0%,#5fb2e0 45%,var(--hero-b) 100%)}
.hero-photo{position:absolute;left:380px;top:0;width:430px;height:319px;background:linear-gradient(90deg,rgba(143,208,239,0),#5b9ec8 40%,#2f5f8a 100%)}
.hero-shadow{left:150px;top:483px;width:760px;height:16px;background:radial-gradient(ellipse at top,rgba(0,0,0,.22),rgba(0,0,0,0) 70%)}
.hero-copy{position:absolute;left:25px;top:0;width:380px;height:319px;color:#fff}
.hero-copy > *{position:absolute;left:0}
.hero-title{top:17px;font-size:24px;font-weight:600;white-space:nowrap;line-height:32px}
.hero-list{top:59px;list-style:none;font-family:"Arimo",sans-serif;font-size:14.5px;line-height:19px;white-space:nowrap}
.hero-list li{position:relative;padding-left:16px}
.hero-list li::before{content:"";position:absolute;left:5px;top:6px;border-left:4px solid var(--orange-light);border-top:3.5px solid transparent;border-bottom:3.5px solid transparent}
.send-label{top:145px;font-size:13.5px;font-weight:500;line-height:18px;white-space:nowrap}
.select{top:173px;width:252px;height:36px;background:#fff;border-radius:3px;display:flex;align-items:center;justify-content:space-between;padding:0 4px 0 10px;color:#333;font-size:14px;font-weight:500}
.select-btn{width:28px;height:28px;border-radius:3px;background:var(--blue-dark);display:flex;align-items:center;justify-content:center}
.or{top:216px;width:252px;display:flex;align-items:center;gap:8px;font-size:13px;line-height:16px}
.or::before,.or::after{content:"";flex:1;height:1px;background:rgba(255,255,255,.7)}
.cta{top:242px;width:252px;height:44px;border-radius:4px;background:linear-gradient(var(--orange-light),#f4a616);border-bottom:2px solid #c9780c;display:flex;align-items:center;justify-content:center;color:#1f1f1f;font-weight:700;font-size:20px;letter-spacing:.5px}
.login-note{top:294px;width:252px;text-align:center;font-size:12.5px;line-height:16px;white-space:nowrap}

/* welcome */
.h2{font-size:21px;font-weight:500;color:var(--blue-dark)}
.welcome{left:124px;top:515px;width:812px}
.welcome p{margin-top:10px;font-size:12px;letter-spacing:-.15px;line-height:19px;color:var(--text)}

/* columns */
.col{top:696px;width:257px}
.col-safety{left:124px}
.col-testimonials{left:401px}
.col-news{left:677px}
.security-img{margin-top:20px;width:256px;height:129px;background:#d6d6d6;padding:9px}
.security-img div{width:100%;height:100%;background:linear-gradient(135deg,#0c2f63,#1d6fc4 55%,#5fc2f2)}
.feat{list-style:none;margin-top:18px;font-size:12px;letter-spacing:-.1px;line-height:19px}
.feat li{position:relative;padding-left:17px;margin-bottom:11px}
.feat li::before{content:"";position:absolute;left:5px;top:6px;border-left:4px solid var(--orange);border-top:3.5px solid transparent;border-bottom:3.5px solid transparent}
.quote{margin-top:22px;font-size:12px;letter-spacing:-.15px;line-height:19px;width:256px}
.quote-by{margin-top:15px;font-size:12px}
.news{margin-top:22px}
.news-item{border-bottom:1px solid var(--rule);padding-bottom:7px;margin-bottom:6px}
.news-item:last-child{border-bottom:none}
.news-date{font-family:"Arimo",sans-serif;font-size:11px;color:#555;line-height:16px}
.news-title{font-size:12px;letter-spacing:-.1px;line-height:18px;color:#222}

/* footer */
.footer-rule{left:124px;top:1033px;width:810px;height:8px;background:radial-gradient(ellipse at top,rgba(0,0,0,.15),rgba(0,0,0,0) 70%);border-top:1px solid #e2e2e2}
.footer-help{left:178px;top:1051px;font-size:19px;font-weight:500;line-height:25px;color:#222;white-space:nowrap}
.footer-help a{color:var(--link);text-decoration:none}
.footer-help .tel{color:var(--orange)}
.footer-line{left:124px;top:1124px;width:810px;height:1px;background:var(--rule)}
.footer-nav{left:124px;top:1141px;display:flex;gap:21px;font-size:12px}
.footer-nav a{color:var(--link);text-decoration:none}
.social{left:824px;top:1138px;display:flex;gap:10px}
.social span{width:20px;height:20px;border-radius:50%;background:#3a3a3a}
.copyright{left:126px;top:1170px;font-size:11.5px;color:#333}
</style>
</head>
<body>
<div class="page">
  <div class="abs header-band"></div>
  <div class="abs brand">
    <div class="brand-name"><span>MERIDALE EXCHANGE</span><span class="brand-dot"></span></div>
    <div class="brand-tag">INTERNATIONAL MONEY TRANSFER</div>
  </div>
  <div class="abs help-top">
    Need Meridale Exchange Help?<br>
    <a href="#">Email us</a> or call us any time <span class="tel">(877) 555-0148</span> (toll free) or <span class="tel">+1 (415) 555-0192</span>
  </div>

  <nav class="abs nav">
    <a class="active" href="#">Home</a>
    <a href="#">Services</a>
    <a href="#">Transfer</a>
    <a href="#">About Us</a>
    <a href="#">Contact Us</a>
    <a href="#">FAQ</a>
  </nav>
  <div class="abs login">LOGIN</div>

  <section class="abs hero">
    <div class="hero-photo" role="img" aria-label="Photo of a smiling couple using a laptop"></div>
    <div class="hero-copy">
      <h1 class="hero-title">Lorem ipsum dolor sit amet</h1>
      <ul class="hero-list">
        <li>Low fees and locked-in exchange rates</li>
        <li>Easy and fast service to 30 countries</li>
        <li>Safe and secure</li>
      </ul>
      <div class="send-label">Send money from the U.S. to:</div>
      <div class="select">Choose a country
        <span class="select-btn"><svg width="10" height="6" viewBox="0 0 10 6"><path d="M0 0h10L5 6z" fill="#fff"/></svg></span>
      </div>
      <div class="or">or</div>
      <div class="cta">GET STARTED</div>
      <div class="login-note">Already have an account? Log in</div>
    </div>
  </section>
  <div class="abs hero-shadow"></div>

  <section class="abs welcome">
    <h2 class="h2">Welcome to Meridale Exchange</h2>
    <p>Lorem ipsum dolor sit amet, consectetur adipisicing elit, sed do eiusmod tempor incididunt ut labore et dolore magna aliqua. Lorem ipsum dolor sit amet, consectetur adipisicing elit, sed do eiusmod tempor incididunt ut labore. Lorem ipsum dolor sit amet, consectetur adipisicing elit, sed do eiusmod tempor incididunt ut labore et dolore magna aliqua. Lorem ipsum dolor sit amet, consectetur adipisicing elit, sed do eiusmod tempor incididunt ut labore. Lorem ipsum dolor sit amet, consectetur adipisicing elit, sed do eiusmod tempor incididunt ut labore et dolore magna aliqua. Lorem ipsum dolor sit amet, consectetur adipisicing elit, sed do eiusmod tempor incididunt ut labore.</p>
  </section>

  <section class="abs col col-safety">
    <h2 class="h2">Safety and Security</h2>
    <div class="security-img"><div role="img" aria-label="Illustration of digital files on a blue circuit background"></div></div>
    <ul class="feat">
      <li>Money-back GUARANTEE for your peace of mind</li>
      <li>Trusted banks and partners</li>
      <li>First class proprietary anti-fraud filters</li>
    </ul>
  </section>

  <section class="abs col col-testimonials">
    <h2 class="h2">Testimonials</h2>
    <p class="quote">“Lorem ipsum dolor sit amet, consectetur adipisicing elit, sed do eiusmod tempor incididunt ut labore et dolore magna aliqua. Lorem ipsum dolor sit amet, consectetur adipisicing elit, sed do eiusmod tempor incididunt ut labore. Lorem ipsum dolor sit amet, consectetur adipisicing elit, sed do eiusmod tempor incididunt ut labore et dolore magna aliqua. Lorem ipsum dolor sit amet, consectetur adipisicing elit, sed do eiusmod tempor incididunt ut labore. ”</p>
    <p class="quote-by">-Lorem ipsum</p>
  </section>

  <section class="abs col col-news">
    <h2 class="h2">Latest News</h2>
    <div class="news">
      <div class="news-item"><div class="news-date">December 12th, 2011</div><div class="news-title">Lorem ipsum dolor sit amet, consectetur adipisicing elit</div></div>
      <div class="news-item"><div class="news-date">December 12th, 2011</div><div class="news-title">Lorem ipsum dolor sit amet, consectetur adipisicing elit</div></div>
      <div class="news-item"><div class="news-date">December 12th, 2011</div><div class="news-title">Lorem ipsum dolor sit amet, consectetur adipisicing elit</div></div>
      <div class="news-item"><div class="news-date">December 12th, 2011</div><div class="news-title">Lorem ipsum dolor sit amet, consectetur adipisicing elit</div></div>
    </div>
  </section>

  <div class="abs footer-rule"></div>
  <div class="abs footer-help">
    Need Meridale Exchange Help?<br>
    <a href="#">Email us</a> or call us any time <span class="tel">(877) 555-0148</span> (toll free) or <span class="tel">+1 (415) 555-0192</span>
  </div>
  <div class="abs footer-line"></div>
  <nav class="abs footer-nav">
    <a href="#">Home</a><a href="#">Services</a><a href="#">Transfer</a><a href="#">About us</a><a href="#">Contact us</a><a href="#">FAQ</a>
  </nav>
  <div class="abs social" aria-label="Social links"><span></span><span></span><span></span><span></span></div>
  <div class="abs copyright">Copyright © 2013 Meridale Exchange. All rights reserved.</div>
</div>
</body>
</html>
```